Dovanne Luxury Landscapes

A landscape business card.

Target Market(s)

Middle aged and up. Professionals.

Industry/Entity Type

Landscape

Contact Information for Business Card

Waverley

Colors
0054AA
0677BA
7BADD7
CADEEF
E8F1F8
0094D4
00A9DD
6FCCEA
C7EBF8
E9F6FB

Requirements
Must have
• The color blue and silver be very attractive
Nice to have
• An embossed logo. A watermark of a plant or something that indicates that we are a landscape company in the background of the backside where list of services are offered. . List of services on the back.
Should not have
• Red, yellow, orange.

```html
<!DOCTYPE html>
<html lang="en">
<head>
<meta charset="utf-8">
<title>Dovanne Luxury Landscapes – Business Card</title>
<link href="https://fonts.googleapis.com/css2?family=Montserrat:wght@400;500;700&display=swap" rel="stylesheet">
<style>
  :root {
    --brand-blue: #2f44a0;
    --card-white: #ffffff;
    --ink: #1e1e24;
    --backdrop: #e6e3de;
    --silver: #e8ebf3;
  }
  * { margin: 0; padding: 0; box-sizing: border-box; }
  html, body { width: 900px; height: 1200px; overflow: hidden; }
  body {
    background: var(--backdrop);
    font-family: "Montserrat", sans-serif;
    position: relative;
  }
  .card {
    position: absolute;
    width: 742px;
    height: 440px;
    border-radius: 22px;
    overflow: hidden;
    box-shadow: 0 6px 14px rgba(0,0,0,0.35);
  }
  .card-front { left: 80px; top: 131px; background: var(--card-white); }
  .card-back { left: 79px; top: 638px; background: var(--brand-blue); }

  .front-band { position: absolute; inset: 0; }

  .wordmark {
    position: absolute;
    left: 36px;
    top: 38px;
    color: var(--brand-blue);
    font-weight: 700;
    line-height: 1;
    text-transform: uppercase;
  }
  .wordmark-name { font-size: 50px; letter-spacing: 1px; display: block; }
  .wordmark-tag { font-size: 21px; letter-spacing: 1.9px; display: block; margin-top: 4px; }

  .name-tab {
    position: absolute; left: 0; top: 157px;
    width: 14px; height: 46px; background: var(--brand-blue);
  }
  .person-name {
    position: absolute; left: 36px; top: 154px;
    font-size: 24px; font-weight: 700; color: var(--brand-blue);
  }
  .person-title {
    position: absolute; left: 36px; top: 188px;
    font-size: 15.5px; color: var(--ink);
  }
  .address {
    position: absolute; left: 38px; top: 229px;
    font-size: 15.5px; line-height: 21px; color: var(--ink); font-style: normal;
  }
  .contact-list {
    position: absolute; left: 36px; top: 310px; list-style: none;
  }
  .contact-list li {
    display: flex; align-items: center; height: 31px;
    font-size: 15.5px; color: var(--ink);
  }
  .contact-list svg { width: 20px; height: 18px; margin-right: 14px; fill: var(--brand-blue); }

  .back-emblem {
    position: absolute; left: 261px; top: 58px; width: 220px; height: 220px;
  }
  .back-wordmark {
    position: absolute; left: 0; right: 0; top: 306px;
    text-align: center; color: var(--silver);
    font-weight: 700; text-transform: uppercase; line-height: 1;
  }
  .back-wordmark .wordmark-name { font-size: 54px; letter-spacing: 1.5px; }
  .back-wordmark .wordmark-tag { font-size: 23px; letter-spacing: 1.2px; margin-top: 6px; }
</style>
</head>
<body>
  <section class="card card-front">
    <svg class="front-band" viewBox="0 0 742 440" aria-hidden="true">
      <polygon points="336,0 552,0 722,440 504,440" fill="var(--brand-blue)"/>
      <line x1="325" y1="0" x2="495" y2="440" stroke="var(--brand-blue)" stroke-width="2"/>
      <line x1="563" y1="0" x2="733" y2="440" stroke="var(--brand-blue)" stroke-width="2"/>
      <circle cx="545" cy="269" r="70" fill="none" stroke="var(--card-white)" stroke-width="3"/>
    </svg>

    <div class="wordmark">
      <span class="wordmark-name">Dovanne</span>
      <span class="wordmark-tag">Luxury Landscapes</span>
    </div>

    <div class="name-tab"></div>
    <h1 class="person-name">Marla Thibodeau</h1>
    <p class="person-title">Managing Director</p>
    <address class="address">18C Alder Lane, Kestrel Bay,<br>Ontario, K7M 4T2</address>

    <ul class="contact-list">
      <li>
        <svg viewBox="0 0 20 18"><path d="M2 5c0-3 16-3 16 0v2h-4V5.5c-2-1-6-1-8 0V7H2z"/><path d="M4 8h12l2 9H2z"/><circle cx="10" cy="12.5" r="2.5" fill="#fff"/></svg>
        613-555-LAWN
      </li>
      <li>
        <svg viewBox="0 0 20 18"><rect x="1" y="3" width="18" height="13" rx="1.5"/><path d="M1.5 4l8.5 6.5L18.5 4" stroke="#fff" stroke-width="1.6" fill="none"/></svg>
        info@Dovanne.com
      </li>
      <li>
        <svg viewBox="0 0 20 18"><circle cx="10" cy="9" r="8.5"/><path d="M5 5c2 0 3 2 2 4s-2 3 0 5M13 3c-1 2 1 3 3 3M12 11c1 1 2 2 1 4" stroke="#fff" stroke-width="1.5" fill="none"/></svg>
        www.Dovanne.com
      </li>
    </ul>
  </section>

  <section class="card card-back">
    <svg class="back-emblem" viewBox="0 0 220 220" aria-hidden="true">
      <circle cx="110" cy="110" r="106" fill="none" stroke="var(--silver)" stroke-width="4"/>
    </svg>
    <div class="back-wordmark">
      <span class="wordmark-name">Dovanne</span>
      <span class="wordmark-tag">Luxury Landscapes</span>
    </div>
  </section>
</body>
</html>
```